Marlowick community hall home page

We are building a modern, responsive website & booking system for our community hall. For this PixelForge task, we would like to receive design ideas for the home page.
There are no limits on the colours or fonts that can be used. We are looking for a modern, fresh design with a local/community feel. We don’t have a logo but we also recognise that our name is quite long! … So initials (MCH) instead of the name would be fine.
People book our community hall for a range of activities including: fitness classes, wedding receptions, birthday parties, business meetings, teaching, community events, charity fundraisers and other celebrations.
We have three main goals for the website. The first is that people can check our calendar and make a booking for an available time slot. The second is that they can read about our facilities and the prices for hiring them. The third is that people can find out about upcoming activities & events.
CTA: Book now
A button that links to a booking request form. (The form is not part of this design project)
Primary/Header navigation:
Home | Calendar | Facilities | Prices | Photos | News | Contact
Secondary/Footer navigation:
Chatterleaf | Quillcast
Login | Register | Privacy policy | Terms & conditions
Example texts (lorem ipsum etc. is also fine):
We have everything you need from a venue, whether it’s an elegant room with ample flexible space, a lavish and elegant hall for a wedding reception, a conference room that fits 125 delegates or a easy access venue to the town centre.
The hall is available for hire for wedding receptions, birthday celebrations, anniversaries, children's parties, presentations, lectures, fitness groups, and will comfortably accommodate all your guests.
This venue is well equipped with a modern kitchen, a range of audio and technical services, hearing loop, licensed bar, conference facilities, disabled access and unlimited free WiFi.
You can use this website to find out more about our rooms, equipment and the services we can offer and use the calendar to see where we have rooms available. You can also book rooms using our online booking system.
To the front of the building is a large public open grassed area across which is a row of shops. To the rear of the building is the large car park, including spaces for blue badge holders and a large enclosed cycle rack. This area also has extensive gardens, with seating and planting areas maintained by local volunteers.
The community hall is run and managed by volunteers of the Marlowick Community Organisation. Our objectives are to increase opportunities for people living in and around Pepperton.
We are passionate about being the heart of the community; caring for this community centred property and visitors are at the heart of all we do.
Where to go next
— Check when the hall is free
— Read our booking policy documents
— Make a booking reservation
Amenities
— Free WiFi
— Free car parking
— Fully equipped kitchen
— Hearing loop
Details for our most popular facilities (rooms):
Name: Main hall
Short description: A 127 square metre main hall with entrance lobby, toilets, a well-equipped kitchen and separate storage facilities. Three sets of double doors provide access to a large paved area and the adjacent playing field.
Capacity: 180 people
Price: £10-20 per hour
Links: More info | Book now
Name: Large meeting room
Short description: A delightful, spacious room with an outlook and access to the small walled garden. Ideal for meetings and small gatherings - it has its own access door and the use of a disabled W/C. We offer a reduced rate for this room when booked together with the main hall.
Capacity: 20 people
Price: £6-12 per hour
Attachments:
We have attached some photos of the hall & some (royalty free) stock images for inspiration.

```html
<!DOCTYPE html>
<html lang="en">
<head>
<meta charset="utf-8">
<title>Marlowick Community Hall</title>
<link href="https://fonts.googleapis.com/css2?family=Poppins:wght@400;500;600;700&display=swap" rel="stylesheet">
<style>
:root{
  --blue:#0b72b5;
  --blue-dark:#075a92;
  --navy:#0d2a44;
  --ink:#22313f;
  --muted:#5b6875;
  --white:#ffffff;
  --line:#d9dee3;
}
*{box-sizing:border-box;margin:0;padding:0}
html,body{width:1200px;height:4280px;overflow:hidden}
body{font-family:"Poppins",Arial,sans-serif;color:var(--ink);background:var(--white);position:relative}
.abs{position:absolute}
.btn{display:inline-block;background:var(--blue);color:var(--white);font-weight:600;font-size:15px;letter-spacing:.5px;padding:14px 30px;border-radius:30px;text-transform:uppercase;box-shadow:0 6px 14px rgba(0,0,0,.18)}
.btn-white{background:var(--white);color:var(--blue)}
.kicker{font-size:13px;font-weight:600;text-transform:uppercase;letter-spacing:.5px}
.heading{font-size:28px;font-weight:700;text-transform:uppercase;line-height:1.1}

/* hero */
.hero{left:0;top:0;width:1200px;height:880px}
.site-nav{left:0;top:0;width:1200px;height:120px}
.brand{left:168px;top:48px;display:flex;align-items:center;gap:14px;color:var(--white);font-size:22px;font-weight:600;line-height:1.05;text-transform:uppercase}
.brand-mark{width:52px;height:52px;border:2px solid var(--white);border-radius:50%}
.menu{right:168px;top:68px;display:flex;gap:26px;list-style:none;color:var(--white);font-size:14px;font-weight:500;text-transform:uppercase}
.hero-title{left:0;top:236px;width:1200px;text-align:center;color:var(--white);font-size:72px;font-weight:700;line-height:1.05;text-transform:uppercase}
.hero-rule{left:400px;top:404px;width:400px;height:2px;background:rgba(255,255,255,.7)}
.hero-cta{left:0;top:466px;width:1200px;text-align:center}

/* about */
.about-photo-a{left:168px;top:872px;width:220px;height:368px;box-shadow:0 8px 20px rgba(0,0,0,.18)}
.about-photo-b{left:280px;top:1024px;width:248px;height:316px;border:6px solid var(--white);box-shadow:0 8px 20px rgba(0,0,0,.2)}
.about-text{left:572px;top:944px;width:520px}
.about-text .heading{color:var(--blue);margin:4px 0 18px}
.about-text p{font-size:13.5px;line-height:1.65;color:var(--muted);margin-bottom:10px}
.about-text .btn{margin-top:14px}

/* where to go next */
.next{left:0;top:1340px;width:1200px;height:880px}
.next-text{left:168px;top:1626px;width:380px;color:var(--white)}
.next-text .heading{margin:2px 0 20px}
.next-text p{font-size:13px;line-height:1.75;opacity:.92}
.next-text .btn{margin-top:30px;font-size:13px}
.calendar{left:652px;top:1652px;width:348px;background:rgba(255,255,255,.93);box-shadow:0 10px 24px rgba(0,0,0,.3)}
.cal-head{height:48px;background:var(--blue);color:var(--white);display:flex;align-items:center;justify-content:space-between;padding:0 12px;font-size:17px;font-weight:600;text-transform:uppercase}
.cal-arrow{width:26px;height:26px;border-radius:50%;background:var(--white)}
.cal-grid{display:grid;grid-template-columns:repeat(7,1fr);padding:8px 10px 12px;font-size:14px;color:var(--muted);text-align:center;row-gap:12px}
.cal-grid .dow{font-weight:600;color:var(--ink)}

/* amenities */
.amen-title{left:0;top:2250px;width:1200px;text-align:center}
.amen-title .heading{color:var(--blue)}
.amenities{left:168px;top:2362px;display:flex;gap:20px}
.amenity{width:200px;height:188px;background:var(--white);box-shadow:0 6px 18px rgba(0,0,0,.14);display:flex;flex-direction:column;align-items:center;justify-content:flex-end;padding-bottom:30px;gap:22px;font-size:14px;font-weight:600;text-transform:uppercase;color:var(--navy);text-align:center}
.amenity.is-active{background:var(--blue);color:var(--white)}

/* facilities */
.facilities{left:0;top:2672px;width:1200px;height:740px}
.fac-title{left:0;top:2770px;width:1200px;text-align:center;color:var(--white)}
.room{top:2880px;width:400px;text-align:center;color:var(--white)}
.room h3{font-size:28px;font-weight:700;text-transform:uppercase;margin:14px 0 16px}
.room p{font-size:12.5px;line-height:1.6;opacity:.92}
.room .meta{margin-top:14px;font-size:12px}
.room .btn{margin-top:30px;font-size:13px;padding:12px 26px}

/* contact */
.contact-photo{left:592px;top:3512px;width:440px;height:336px}
.contact-card{left:168px;top:3560px;width:464px;height:264px;background:var(--white);box-shadow:0 8px 24px rgba(0,0,0,.14);padding:30px 40px}
.contact-card .heading{color:var(--blue);margin:2px 0 18px}
.contact-item{display:flex;align-items:center;gap:14px;font-size:13px;line-height:1.45;color:var(--muted);margin-bottom:12px}
.contact-icon{flex:none;width:34px;height:34px;border-radius:50%;background:var(--blue);display:flex;align-items:center;justify-content:center}

/* footer */
.footer-links{left:0;top:3996px;width:1200px;text-align:center;font-size:13px;font-weight:600;color:var(--navy);line-height:1.9;text-transform:uppercase}
.footer-rule{left:168px;top:4088px;width:864px;height:1px;background:var(--line)}
.copyright{left:168px;top:4116px;font-size:13px;font-weight:600;color:var(--navy);text-transform:uppercase}
.social{right:168px;top:4108px;display:flex;gap:12px}
.social span{width:30px;height:30px;border-radius:50%;background:var(--blue)}
</style>
</head>
<body>

<!-- HERO -->
<section class="hero abs">
  <svg width="1200" height="880" viewBox="0 0 1200 880" class="abs" style="left:0;top:0">
    <defs>
      <linearGradient id="heroFill" x1="0" y1="0" x2="1" y2="1">
        <stop offset="0" stop-color="#1b2c4e"/><stop offset=".5" stop-color="#2f4f86"/><stop offset="1" stop-color="#141d33"/>
      </linearGradient>
    </defs>
    <path role="img" aria-label="Photo of a crowded evening event inside the hall" d="M0 0H1200V690C1120 690 1090 760 1010 820C960 860 900 870 800 870H400C300 870 240 860 190 820C110 760 80 690 0 690Z" fill="url(#heroFill)"/>
    <path d="M0 0H1200V690C1120 690 1090 760 1010 820C960 860 900 870 800 870H400C300 870 240 860 190 820C110 760 80 690 0 690Z" fill="rgba(0,0,0,.25)"/>
  </svg>
  <header class="site-nav abs">
    <div class="brand abs"><span class="brand-mark"></span><span>Marlowick<br>Community Hall</span></div>
    <ul class="menu abs"><li>Home</li><li>Calendar</li><li>Facilities</li><li>Prices</li><li>Photos</li><li>News</li><li>Contact</li></ul>
  </header>
  <h1 class="hero-title abs">Marlowick Community<br>Hall</h1>
  <div class="hero-rule abs"></div>
  <div class="hero-cta abs"><span class="btn btn-white">Book now</span></div>
</section>

<!-- ABOUT -->
<div class="about-photo-a abs" role="img" aria-label="Photo of a white flower table centrepiece" style="background:linear-gradient(160deg,#e9ecef,#b7bec6 60%,#7d8792)"></div>
<div class="about-photo-b abs" role="img" aria-label="Photo of a wedding table with peach flowers and glassware" style="background:linear-gradient(170deg,#d8b89a,#b97c5a 50%,#5d4a3c)"></div>
<section class="about-text abs">
  <div class="kicker">About</div>
  <h2 class="heading">Marlowick Community Hall</h2>
  <p>We have everything you need from a venue, whether it's an elegant room with ample flexible space, a lavish and elegant hall for a wedding reception, a conference room that fits 125 delegates or a easy access venue to the town centre.</p>
  <p>The hall is available for hire for wedding receptions, birthday celebrations, anniversaries, children's parties, presentations, lectures, fitness groups, and will comfortably accommodate all your guests.</p>
  <span class="btn">Book now</span>
</section>

<!-- WHERE TO GO NEXT -->
<section class="next abs">
  <svg width="1200" height="880" viewBox="0 0 1200 880" class="abs" style="left:0;top:0">
    <defs>
      <clipPath id="nextShape"><path d="M0 110C180 110 300 0 600 0C900 0 1020 110 1200 110V770C1020 770 900 880 600 880C300 880 180 770 0 770Z"/></clipPath>
      <linearGradient id="nextPhoto" x1="0" y1="0" x2="1" y2="1"><stop offset="0" stop-color="#6b5a4a"/><stop offset=".5" stop-color="#3e342d"/><stop offset="1" stop-color="#8a7a68"/></linearGradient>
    </defs>
    <g clip-path="url(#nextShape)">
      <rect x="0" y="0" width="600" height="880" fill="var(--blue)"/>
      <rect role="img" aria-label="Photo of the hall set with round dining tables under a chandelier" x="600" y="0" width="600" height="880" fill="url(#nextPhoto)"/>
    </g>
  </svg>
</section>
<div class="next-text abs">
  <div class="kicker">MCH</div>
  <h2 class="heading">Where to go next</h2>
  <p>To the front of the building is a large public open grassed area across which is a row of shops. To the rear of the building is the large car park, including spaces for blue badge holders and a large enclosed cycle rack. This area also has extensive gardens, with seating and planting areas maintained by local volunteers.</p>
  <span class="btn btn-white">Read booking policy documents</span>
</div>
<div class="calendar abs">
  <div class="cal-head"><span class="cal-arrow"></span>November<span class="cal-arrow"></span></div>
  <div class="cal-grid">
    <span class="dow">M</span><span class="dow">T</span><span class="dow">W</span><span class="dow">T</span><span class="dow">F</span><span class="dow">S</span><span class="dow">S</span>
    <span></span><span></span><span></span><span></span><span></span><span></span><span>1</span>
    <span>2</span><span>3</span><span>4</span><span>5</span><span>6</span><span>7</span><span>8</span>
    <span>9</span><span>10</span><span>11</span><span>12</span><span>13</span><span>14</span><span>15</span>
    <span>16</span><span>17</span><span>18</span><span>19</span><span>20</span><span>21</span><span>22</span>
    <span>23</span><span>24</span><span>25</span><span>26</span><span>27</span><span>28</span><span>29</span>
    <span>30</span>
  </div>
</div>

<!-- AMENITIES -->
<div class="amen-title abs"><div class="kicker">About</div><h2 class="heading">MCH Amenities</h2></div>
<section class="amenities abs">
  <div class="amenity is-active">
    <svg width="64" height="52" viewBox="0 0 64 52" fill="none" stroke="#fff" stroke-width="5" stroke-linecap="round"><path d="M4 18a40 40 0 0 1 56 0"/><path d="M14 28a26 26 0 0 1 36 0"/><path d="M24 38a12 12 0 0 1 16 0"/><circle cx="32" cy="47" r="3" fill="#fff"/></svg>
    Free WiFi
  </div>
  <div class="amenity">
    <svg width="64" height="56" viewBox="0 0 64 56" fill="var(--navy)"><path d="M32 0a10 10 0 0 0-10 10c0 8 10 18 10 18s10-10 10-18A10 10 0 0 0 32 0zm0 14a4 4 0 1 1 0-8 4 4 0 0 1 0 8z"/><path d="M12 32h40l6 10v10H6V42z"/><circle cx="16" cy="52" r="4" fill="#fff"/><circle cx="48" cy="52" r="4" fill="#fff"/></svg>
    Free car parking
  </div>
  <div class="amenity">
    <svg width="64" height="56" viewBox="0 0 64 56" fill="none" stroke="var(--blue)" stroke-width="3"><rect x="8" y="18" width="48" height="34"/><line x1="8" y1="28" x2="56" y2="28"/><rect x="16" y="34" width="32" height="12"/><path d="M18 4v10M26 4v10M38 4v10M46 4v10"/></svg>
    Fully equipped<br>kitchen
  </div>
  <div class="amenity">
    <svg width="48" height="56" viewBox="0 0 48 56" fill="none" stroke="var(--navy)" stroke-width="3.5" stroke-linecap="round"><path d="M10 22a16 16 0 0 1 32 0c0 10-10 12-10 22a8 8 0 0 1-14 4"/><path d="M18 22a8 8 0 0 1 16 0c0 5-6 6-6 10"/></svg>
    Hearing loop
  </div>
</section>

<!-- FACILITIES -->
<section class="facilities abs">
  <svg width="1200" height="740" viewBox="0 0 1200 740" class="abs" style="left:0;top:0">
    <defs>
      <clipPath id="facShape"><path d="M0 110C180 110 300 0 600 0C900 0 1020 110 1200 110V630C1020 630 900 740 600 740C300 740 180 630 0 630Z"/></clipPath>
      <linearGradient id="facLeft" x1="0" y1="0" x2="1" y2="1"><stop offset="0" stop-color="#2c3340"/><stop offset="1" stop-color="#111722"/></linearGradient>
      <linearGradient id="facRight" x1="0" y1="0" x2="1" y2="1"><stop offset="0" stop-color="#1a86c8"/><stop offset="1" stop-color="#075a92"/></linearGradient>
    </defs>
    <g clip-path="url(#facShape)">
      <rect role="img" aria-label="Photo of the main hall laid out for a dinner" x="0" y="0" width="600" height="740" fill="url(#facLeft)"/>
      <rect role="img" aria-label="Photo of the meeting room tinted blue" x="600" y="0" width="600" height="740" fill="url(#facRight)"/>
    </g>
  </svg>
</section>
<div class="fac-title abs"><div class="kicker">MCH</div><h2 class="heading">Most popular facilities</h2></div>
<div class="room abs" style="left:160px">
  <svg width="70" height="56" viewBox="0 0 70 56" fill="none" stroke="#fff" stroke-width="3"><rect x="14" y="14" width="42" height="14"/><path d="M14 28l-6 24M56 28l6 24M24 28v24M46 28v24"/><circle cx="22" cy="7" r="4"/><circle cx="35" cy="7" r="4"/><circle cx="48" cy="7" r="4"/></svg>
  <h3>Main hall</h3>
  <p>A 127 square metre main hall with entrance lobby, toilets, a well-equipped kitchen and separate storage facilities. Three sets of double doors provide access to a large paved area.</p>
  <p class="meta">Capacity: 180 people | Price: £10-20 per hour | More info</p>
  <span class="btn btn-white">Book now</span>
</div>
<div class="room abs" style="left:640px">
  <svg width="70" height="56" viewBox="0 0 70 56" fill="none" stroke="#fff" stroke-width="3"><rect x="28" y="4" width="38" height="26"/><circle cx="14" cy="12" r="6"/><path d="M6 40v-12h16l8-6M4 40h62M12 40v14M58 40v14"/></svg>
  <h3>Large meeting room</h3>
  <p>A delightful, spacious room with an outlook and access to the small walled garden. Ideal for meetings and small gatherings - it has its own access door.</p>
  <p class="meta">Capacity: 20 people | Price: £6-12 per hour | More info</p>
  <span class="btn btn-white">Book now</span>
</div>

<!-- CONTACT -->
<div class="contact-photo abs" role="img" aria-label="Photo of a table with pink and red flowers and wine glasses" style="background:linear-gradient(150deg,#f1e4e4,#c9707a 45%,#5f7a5a)"></div>
<section class="contact-card abs">
  <div class="kicker" style="color:var(--ink)">MCH</div>
  <h2 class="heading">Contact us</h2>
  <div class="contact-item"><span class="contact-icon"><svg width="14" height="18" viewBox="0 0 14 18" fill="#fff"><path d="M7 0a7 7 0 0 0-7 7c0 5 7 11 7 11s7-6 7-11a7 7 0 0 0-7-7zm0 10a3 3 0 1 1 0-6 3 3 0 0 1 0 6z"/></svg></span>Duis aute irure dolor in reprehenderit<br>in voluptate</div>
  <div class="contact-item"><span class="contact-icon"><svg width="16" height="16" viewBox="0 0 16 16" fill="#fff"><path d="M3 0l3 4-2 2c1 2 4 5 6 6l2-2 4 3-2 3C7 16 0 9 0 3z"/></svg></span>Phone: 01632 960 418<br>Fax: 01632 960 419</div>
  <div class="contact-item"><span class="contact-icon"><svg width="16" height="12" viewBox="0 0 16 12" fill="none" stroke="#fff" stroke-width="1.6"><rect x="1" y="1" width="14" height="10"/><path d="M1 1l7 6 7-6"/></svg></span>Email: info@marlowick<br>communityhall</div>
</section>

<!-- FOOTER -->
<footer>
  <div class="footer-links abs">Login | Register | Privacy policy | Terms &amp; conditions<br>Home | Calendar | Facilities | Prices | Photos | News | Contact</div>
  <div class="footer-rule abs"></div>
  <div class="copyright abs">Copyrights © 2021 Marlowick Community Hall</div>
  <div class="social abs"><span aria-label="Chatterleaf"></span><span aria-label="Quillcast"></span></div>
</footer>

</body>
</html>
```